" Cavalto Solutions oferece serviços de automação de tarefas manuais repetitivas realizadas na administração das empresas, como ingresso de faturas, coleta de dados de vários sistemas e consolidação manual, aceso a site para extração de dados e posterior registro em sistemas próprios, etc. Os serviços que oferece são: a identificação dessas oportunidades apoiando no budiness case, o desenvolvimento dos robôs para automação, a implantação do modelo de governança para assegurar a boa implantação e posterior sustentabilidade, transferência de conhecimento para as equipes internos, e finalmente o suporte e manutenção da plataforma. "

```html
<!DOCTYPE html>
<html lang="pt-BR">
<head>
<meta charset="UTF-8">
<title>Cavalto Solutions — Automação Robótica de Processos</title>
<link rel="stylesheet" href="https://fonts.googleapis.com/css2?family=Montserrat:wght@400;600;800&family=Open+Sans:wght@400;600&display=swap">
<style>
  :root{
    --brand:#2aa6d9;
    --brand-dark:#1b86b8;
    --navy:#0b2542;
    --navy-mid:#17466f;
    --sky:#5cc3ea;
    --ink:#3c4650;
    --muted:#7d8790;
    --white:#ffffff;
    --line:#d6dde3;
  }
  *{margin:0;padding:0;box-sizing:border-box}
  html,body{width:1200px;height:1200px;overflow:hidden;background:var(--white)}
  body{font-family:"Open Sans",Arial,sans-serif;color:var(--ink)}
  .site{width:1200px;height:1200px;position:relative}

  .topbar{height:40px;background:var(--brand);display:flex;justify-content:flex-end;align-items:center;padding:0 60px;gap:10px;color:var(--white);font-size:15px;font-weight:600}
  .topbar svg{width:16px;height:16px}

  .header{height:120px;display:flex;align-items:center;justify-content:space-between;padding:0 60px;border-bottom:1px solid var(--line)}
  .brand{display:flex;align-items:center;gap:14px}
  .brand-mark{width:34px;height:34px;background:var(--brand)}
  .brand-name{font-family:"Montserrat",Arial,sans-serif;font-weight:800;font-size:34px;color:var(--navy-mid);letter-spacing:1px;text-transform:uppercase}
  .nav{display:flex;gap:38px;font-family:"Montserrat",Arial,sans-serif;font-size:18px;font-weight:600;color:var(--ink)}
  .nav .active{color:var(--brand);border-bottom:3px solid var(--brand);padding-bottom:6px}

  .hero{position:relative;height:560px;overflow:hidden}
  .hero-visual{position:absolute;inset:0;background:
      radial-gradient(circle at 72% 40%, #6f8fa8 0%, #3d6386 22%, transparent 48%),
      linear-gradient(100deg, var(--navy) 0%, #123a60 45%, #1d4f7c 70%, #0e2c4d 100%)}
  .hero-content{position:relative;padding:90px 70px 0;max-width:760px}
  .hero-title{font-family:"Montserrat",Arial,sans-serif;font-weight:800;font-size:60px;line-height:1.08;color:var(--white);text-transform:uppercase}
  .hero-text{margin-top:26px;font-size:19px;line-height:1.5;color:var(--sky);font-weight:600;max-width:560px}
  .hero-button{display:inline-block;margin-top:34px;background:var(--brand);color:var(--white);font-family:"Montserrat",Arial,sans-serif;font-weight:600;font-size:19px;padding:14px 36px;border-radius:30px}
  .slider-dots{position:absolute;right:110px;bottom:150px;display:flex;gap:12px}
  .slider-dots span{width:12px;height:12px;border-radius:50%;border:2px solid var(--white)}
  .slider-dots span.on{background:var(--white)}
  .slider-arrow{position:absolute;bottom:140px;width:30px;height:30px}
  .slider-arrow.prev{right:185px}
  .slider-arrow.next{right:60px}

  .services{text-align:center;padding:70px 150px 0}
  .services-title{font-family:"Montserrat",Arial,sans-serif;font-weight:400;font-size:40px;color:var(--navy-mid);display:inline-block;padding:0 40px;position:relative}
  .services-rule{width:120px;height:3px;background:var(--brand);margin:20px auto 40px}
  .services-text{font-size:18px;line-height:1.7;color:var(--muted)}
</style>
</head>
<body>
<div class="site">
  <div class="topbar">
    <svg viewBox="0 0 24 24" fill="none" stroke="#fff" stroke-width="2.2"><path d="M5 3h4l2 5-2.5 1.5a11 11 0 0 0 6 6L16 13l5 2v4a2 2 0 0 1-2 2A16 16 0 0 1 3 5a2 2 0 0 1 2-2z"/></svg>
    <span>(11) 4000-1234</span>
  </div>

  <header class="header">
    <div class="brand">
      <div class="brand-mark"></div>
      <div class="brand-name">Cavalto Solutions</div>
    </div>
    <nav class="nav">
      <span class="active">Home</span>
      <span>Quem Somos</span>
      <span>RPA</span>
      <span>Serviços ▾</span>
      <span>Contato</span>
    </nav>
  </header>

  <section class="hero">
    <div class="hero-visual" role="img" aria-label="Robô humanoide pensativo diante de uma rede de ícones digitais em tons de azul"></div>
    <div class="hero-content">
      <h1 class="hero-title">Automação Robótica de Processos</h1>
      <p class="hero-text">Implantação de RPA - Robotic Process Automation com metodologias ágeis que garantem o fácil e rápido entrega de valor para o negócio.</p>
      <span class="hero-button">Saiba mais</span>
    </div>
    <svg class="slider-arrow prev" viewBox="0 0 24 24" fill="none" stroke="#fff" stroke-width="2.5"><path d="M15 5l-7 7 7 7"/></svg>
    <div class="slider-dots"><span class="on"></span><span></span><span></span></div>
    <svg class="slider-arrow next" viewBox="0 0 24 24" fill="none" stroke="#fff" stroke-width="2.5"><path d="M9 5l7 7-7 7"/></svg>
  </section>

  <section class="services">
    <h2 class="services-title">Confira nossos serviços</h2>
    <div class="services-rule"></div>
    <p class="services-text">A CAVALTO SOLUTIONS possui experiência e know-how diferenciados, atuando em todas as etapas de serviços de suas necessidades de automação robótica de processos.</p>
  </section>
</div>
</body>
</html>
```